use my brand and make an elegant business card  with it

Target Market(s)
male and female ' ages 25 to 45 age- who appreciate the highest quality goods, experiences, services, brands and relationships
Industry/Entity Type
Business
Requirements
Must have
- my logo integrated into the design-note the uploaded file
front: just logo and the phrase: New. Trend. Life. Style
back informations:
Mirela Dostan
Director
phone: +1 604 5290417
www.midostan.com
email: mireladostan@midostan.com
the pin of Facebook (F) and tweeter (T)
Nice to have
- contrast of the colors black gold and silver
Should not have
- cartoons or whimsical design

```html
<!DOCTYPE html>
<html lang="en">
<head>
<meta charset="utf-8">
<title>Midostan — Business Card</title>
<link rel="stylesheet" href="https://fonts.googleapis.com/css2?family=Cinzel:wght@400;500&display=swap">
<style>
  :root {
    --page: #ffffff;
    --ink: #1c1c1c;
    --card-dark: #050505;
    --card-dark-mid: #2a2a2a;
    --gold: #a8841f;
    --gold-line: #8c7330;
    --silver: #9a9a9a;
    --soft-grey: #7d7d7d;
    --card-light: #fbfbfb;
    --hex-tone: #eeeeee;
    --border: #6b6b6b;
    --white: #ffffff;
  }
  * { box-sizing: border-box; margin: 0; padding: 0; }
  html, body { width: 1200px; height: 900px; overflow: hidden; background: var(--page); }
  body { position: relative; font-family: "Cinzel", "Times New Roman", serif; color: var(--ink); }

  .card { position: absolute; overflow: hidden; }

  /* front */
  .card--front {
    left: 312px; top: 104px; width: 576px; height: 334px;
    background: var(--card-dark);
  }
  .front-texture {
    position: absolute; inset: 0;
    background: radial-gradient(ellipse 60% 70% at 48% 42%, var(--card-dark-mid) 0%, #151515 45%, var(--card-dark) 100%);
  }
  .front-frame {
    position: absolute; left: 12px; top: 13px; width: 552px; height: 309px;
    border: 1px solid var(--gold-line);
  }
  .front-brand {
    position: absolute; left: 0; right: 0; top: 150px;
    text-align: center; font-size: 62px; font-weight: 500;
    color: var(--gold); letter-spacing: 4px; line-height: 1;
  }
  .front-tagline {
    position: absolute; left: 0; right: 0; top: 258px;
    text-align: center; font-size: 14px; color: var(--white);
    font-variant: small-caps; text-transform: lowercase;
    text-shadow: 0 0 6px rgba(255,255,255,0.45);
  }
  .front-tagline::first-letter { text-transform: uppercase; }

  /* back */
  .card--back {
    left: 312px; top: 464px; width: 574px; height: 326px;
    background: var(--card-light); border: 1px solid var(--border);
  }
  .back-texture {
    position: absolute; inset: 0;
    background: linear-gradient(180deg, var(--hex-tone) 0%, var(--card-light) 70%);
  }
  .back-tagline {
    position: absolute; left: 0; right: 0; top: 18px; text-align: center;
    font-size: 14px; color: var(--soft-grey); font-variant: small-caps;
  }
  .divider {
    position: absolute; left: 302px; top: 62px; width: 2px; height: 228px;
    background: var(--gold);
  }
  .holder { position: absolute; left: 20px; top: 128px; width: 276px; text-align: center; }
  .holder-name { font-size: 34px; color: var(--gold); font-variant: small-caps; line-height: 1; }
  .holder-role { margin-top: 6px; font-size: 13px; color: var(--ink); text-transform: uppercase; }

  .contact { position: absolute; left: 322px; display: flex; align-items: center; gap: 6px; color: var(--ink); }
  .contact svg { flex: none; }
  .contact--phone { top: 118px; font-size: 25px; }
  .contact--mail { top: 172px; font-size: 12px; text-transform: uppercase; }

  .corner-mark { position: absolute; left: 14px; top: 251px; }
  .website {
    position: absolute; left: 67px; top: 290px; font-size: 18px;
    text-transform: uppercase; color: var(--ink);
  }
  .website .domain { color: var(--gold); }

  .social { position: absolute; left: 352px; top: 286px; display: flex; gap: 4px; }
  .social span { width: 22px; height: 22px; border-radius: 50%; background: var(--ink); display: block; }
  .back-brand {
    position: absolute; left: 412px; top: 287px; font-size: 22px;
    color: var(--gold); font-weight: 500; letter-spacing: 1px; line-height: 1;
  }

  /* previews */
  .preview { position: absolute; left: 1064px; width: 88px; }
  .preview--front { top: 693px; height: 67px; background: var(--card-dark); }
  .preview--front::after {
    content: ""; position: absolute; left: 3px; top: 3px; right: 3px; bottom: 3px;
    border: 1px solid var(--gold-line);
  }
  .preview--front .mini-bar { position: absolute; left: 18px; top: 30px; width: 52px; height: 8px; background: var(--gold); opacity: .8; }
  .preview--back { top: 766px; height: 65px; background: var(--card-light); border: 1px solid var(--border); }
  .preview--back .mini-rule { position: absolute; left: 60px; top: 10px; width: 1px; height: 46px; background: var(--gold); }
  .preview--back .mini-name { position: absolute; left: 8px; top: 28px; width: 44px; height: 4px; background: var(--gold); }
  .preview--back .mini-line { position: absolute; left: 64px; height: 3px; background: var(--silver); }
</style>
</head>
<body>

<section class="card card--front" aria-label="Card front">
  <div class="front-texture" role="img" aria-label="Dark background with a subtle honeycomb texture"></div>
  <div class="front-frame"></div>
  <div class="front-brand">MIDOSTAN</div>
  <p class="front-tagline">New trend lifestyle.</p>
</section>

<section class="card card--back" aria-label="Card back">
  <div class="back-texture" role="img" aria-label="Light background with a faint honeycomb texture"></div>
  <p class="back-tagline">New trend lifestyle</p>
  <div class="divider"></div>

  <div class="holder">
    <p class="holder-name">Mirela Dostan</p>
    <p class="holder-role">Director</p>
  </div>

  <p class="contact contact--phone">
    <svg width="32" height="32" viewBox="0 0 32 32" aria-hidden="true">
      <circle cx="16" cy="16" r="14.5" fill="none" stroke="#1c1c1c" stroke-width="2"/>
      <path d="M11 8.5c1.2-.6 2 .2 2.6 1.6l1 2.2c.3.8 0 1.4-.7 1.9l-.8.6c.6 1.8 2 3.6 3.6 4.6l.7-.7c.6-.6 1.2-.8 1.9-.4l2.1 1.2c1.3.8 1.8 1.7 1 2.7-.9 1.2-2.3 2-3.9 1.6-4.4-1.1-8.2-5.6-8.9-9.8-.3-1.5.3-2.8 1.4-3.5z" fill="#1c1c1c"/>
    </svg>
    +1 604 5290417
  </p>
  <p class="contact contact--mail">
    <svg width="32" height="32" viewBox="0 0 32 32" aria-hidden="true">
      <circle cx="16" cy="16" r="14.5" fill="none" stroke="#1c1c1c" stroke-width="2"/>
      <rect x="8" y="10.5" width="16" height="11" rx="1" fill="#1c1c1c"/>
      <path d="M8.5 11l7.5 6 7.5-6" fill="none" stroke="#fbfbfb" stroke-width="1.2"/>
    </svg>
    mireladostan@midostan.com
  </p>

  <svg class="corner-mark" width="50" height="58" viewBox="0 0 50 58" aria-hidden="true">
    <polygon points="0,0 0,58 50,58" fill="#333333"/>
  </svg>
  <p class="website">www.<span class="domain">midostan</span>.com</p>

  <div class="social" aria-label="Social profiles"><span></span><span></span></div>
  <p class="back-brand">MIDOSTAN</p>
</section>

<div class="preview preview--front" aria-hidden="true"><span class="mini-bar"></span></div>
<div class="preview preview--back" aria-hidden="true">
  <span class="mini-rule"></span>
  <span class="mini-name"></span>
  <span class="mini-line" style="top:24px;width:18px"></span>
  <span class="mini-line" style="top:34px;width:20px"></span>
  <span class="mini-line" style="top:52px;width:14px;background:var(--gold)"></span>
</div>

</body>
</html>
```